Summer Drinks Flyer for Coffee Shop

We are a coffee shop in London and would like to have a cool and nice flyer for our summer drinks (juices and frozen drink) flyer - see on the attached file for the list

Attached you can find an "attempt" - please note that I would no necessary need the image below.

I also attache our new logo.

thank you

Industry/Entity Type

Coffee Shop

```html
<!DOCTYPE html>
<html lang="en">
<head>
<meta charset="UTF-8">
<title>Summer Drinks</title>
<link href="https://fonts.googleapis.com/css2?family=Archivo+Black&family=Arimo:wght@400;700&family=Patrick+Hand&display=swap" rel="stylesheet">
<style>
  :root {
    --page-bg: #ffffff;
    --frame: #222222;
    --title: #f7b12f;
    --title-edge: #fbd27a;
    --frozen: #52ef8a;
    --juice: #5cc40c;
    --coffee: #d3402a;
    --sand: #dcc67e;
    --sand-light: #e8d89c;
  }
  * { margin: 0; padding: 0; box-sizing: border-box; }
  html, body { width: 1200px; height: 900px; overflow: hidden; background: var(--page-bg); }
  .canvas { position: relative; width: 1200px; height: 900px; }
  .flyer {
    position: absolute; left: 279px; top: -1px; width: 647px; height: 901px;
    border: 1px solid var(--frame); background: var(--page-bg);
  }
  .title {
    position: absolute; left: 0; width: 100%; top: 14px; text-align: center;
    font-family: "Archivo Black", "Arial Black", sans-serif; font-size: 51px; line-height: 58px; letter-spacing: 0.5px;
    color: var(--title); -webkit-text-stroke: 1.5px var(--title-edge);
  }
  .heading, .price {
    position: absolute; font-family: "Patrick Hand", cursive; font-size: 46px; line-height: 44px; font-weight: 400;
  }
  .heading { letter-spacing: 1px; }
  .price { left: 477px; letter-spacing: 3px; }
  .items { position: absolute; list-style: none; font-family: "Arimo", Arial, sans-serif; font-size: 24px; line-height: 29px; }
  .extra { position: absolute; left: 143px; font-family: "Arimo", Arial, sans-serif; font-size: 24px; line-height: 29px; }
  .extra b { font-weight: 700; font-size: 26px; margin-right: 6px; }
  .frozen { color: var(--frozen); }
  .juice { color: var(--juice); }
  .coffee { color: var(--coffee); }
  .shop-name {
    position: absolute; left: 48px; top: 838px;
    font-family: "Arimo", Arial, sans-serif; font-size: 30px; line-height: 36px; color: var(--coffee);
  }
  .palms { position: absolute; left: 368px; top: 760px; width: 250px; height: 128px; }
  .sand { position: absolute; left: 26px; top: 876px; }
</style>
</head>
<body>
<div class="canvas">
  <div class="flyer">
    <h1 class="title">SUMMER DRINKS</h1>

    <h2 class="heading frozen" style="left:50px; top:120px;">Frozen Fruit Drinks</h2>
    <span class="price frozen" style="top:120px;">£2.95</span>
    <ul class="items frozen" style="left:74px; top:173px;">
      <li>Strawberry and Banana</li>
      <li>Pineapple, Mango and Banana</li>
    </ul>

    <h2 class="heading juice" style="left:50px; top:252px;">Fruit Juices</h2>
    <span class="price juice" style="top:252px;">£2.95</span>
    <ul class="items juice" style="left:77px; top:313px;">
      <li>Orange and Carrot</li>
      <li>Orange and Pineapple</li>
      <li>Pineapple and Apple</li>
      <li>Apple and Kiwi</li>
      <li>Carrot and Ginger</li>
    </ul>
    <p class="extra juice" style="top:480px;"><b>+</b>Add Mint or Ginger for Free!</p>

    <h2 class="heading coffee" style="left:50px; top:534px;">Iced-Coffees</h2>
    <span class="price coffee" style="top:534px;">£2.45</span>
    <ul class="items coffee" style="left:84px; top:589px;">
      <li>Iced Coffee</li>
      <li>Iced Latte</li>
      <li>Iced Chocolate Drink</li>
    </ul>
    <p class="extra coffee" style="top:694px;"><b>+</b>Add Syrup Shot for 10p</p>

    <svg class="sand" width="590" height="18" viewBox="0 0 590 18">
      <path d="M0 14 Q290 6 590 12 L590 18 L0 18 Z" fill="var(--sand)"/>
    </svg>
    <svg class="palms" viewBox="0 0 250 128" role="img" aria-label="Illustration of three palm trees on a beach">
      <defs>
        <linearGradient id="palmTone" x1="0" y1="0" x2="0" y2="1">
          <stop offset="0" stop-color="var(--sand-light)"/>
          <stop offset="1" stop-color="var(--sand)"/>
        </linearGradient>
      </defs>
      <rect width="250" height="128" rx="10" fill="url(#palmTone)"/>
    </svg>

    <p class="shop-name">Maple Lane Café</p>
  </div>
</div>
</body>
</html>
```